Machining Business Order Thank You Insert

I am looking for a business style card to include with orders that I ship. The card needs to thank the recipient for their order, and encourage them to leave a review. The card should include my business name and contact information and have an area to hand write a message.

I mainly sale on Crafvine and my own website. We are a machining an manufacturing business that are in the sale of mostly metal machined and 3d printed plastic products.

The front of the card should include the following:
Logo: (attached)
Snapgrid: https://www.instagram.com/quillforge/
Friendwall: https://www.facebook.com/QuillForge
Website: https://www.quillforge-example.com/

The back of the card needs an area to write a message

Industry/Entity Type

3D Printing, Machining, Crafvine

Contact Information for Business Card

Black or white front, white back to write a personal message

Font styles to use
Sans Serif

Colors

Designer to choose colors to be used in the design.

Requirements
Must have
• Encourage a review, social media info

```html
<!DOCTYPE html>
<html lang="en">
<head>
<meta charset="utf-8">
<title>QuillForge Order Thank You Card</title>
<link rel="stylesheet" href="https://fonts.googleapis.com/css2?family=Roboto:wght@400;500&family=Dancing+Script:wght@500&display=swap">
<style>
  :root {
    --backdrop: #2b2b2b;
    --card: #ffffff;
    --ink-grey: #6b6b6b;
    --ink-dark: #4a4a4a;
    --accent: #e8582a;
    --accent-soft: #f7d3c4;
    --grey-soft: #dedede;
    --rule: #8a8a8a;
  }
  * { margin: 0; padding: 0; box-sizing: border-box; }
  html, body {
    width: 1200px;
    height: 900px;
    overflow: hidden;
    background: var(--backdrop);
  }
  .canvas {
    position: relative;
    width: 1200px;
    height: 900px;
  }
  .card {
    position: absolute;
    width: 620px;
    height: 354px;
    background: var(--card);
    box-shadow: 0 12px 30px rgba(0, 0, 0, 0.45);
    overflow: hidden;
  }
  .card-front { left: 70px; top: 60px; }
  .card-back { left: 510px; top: 486px; }

  .motif-front {
    position: absolute;
    right: 0;
    top: 0;
    width: 300px;
    height: 240px;
    background: linear-gradient(225deg, var(--accent-soft) 0%, rgba(247, 211, 196, 0.35) 55%, rgba(255, 255, 255, 0) 100%);
  }
  .motif-back {
    position: absolute;
    left: 0;
    top: 0;
    width: 300px;
    height: 354px;
    background: linear-gradient(135deg, var(--grey-soft) 0%, rgba(222, 222, 222, 0.4) 55%, rgba(255, 255, 255, 0) 100%);
  }

  .brand {
    position: absolute;
    left: 56px;
    top: 60px;
    display: flex;
    flex-direction: column;
    gap: 22px;
  }
  .brand-square {
    width: 96px;
    height: 96px;
    background: var(--accent);
  }
  .brand-name {
    font-family: "Roboto", sans-serif;
    font-weight: 500;
    font-size: 30px;
    letter-spacing: 10px;
    color: var(--ink-grey);
  }

  .contact-list {
    position: absolute;
    left: 56px;
    bottom: 28px;
    list-style: none;
    font-family: "Roboto", sans-serif;
    font-size: 17px;
    color: var(--ink-dark);
  }
  .contact-item {
    display: flex;
    align-items: center;
    gap: 12px;
    line-height: 26px;
  }
  .contact-dot {
    width: 13px;
    height: 13px;
    border-radius: 50%;
    background: var(--accent);
  }
  .contact-globe { width: 13px; height: 13px; }

  .thanks {
    position: absolute;
    right: 56px;
    top: 20px;
    text-align: right;
    font-family: "Dancing Script", cursive;
    font-weight: 500;
  }
  .thanks-title {
    display: block;
    font-size: 84px;
    line-height: 1;
    color: var(--accent);
  }
  .thanks-sub {
    display: block;
    font-size: 28px;
    color: var(--ink-grey);
    margin-top: -4px;
  }
  .message-lines {
    position: absolute;
    right: 50px;
    top: 150px;
    width: 330px;
    list-style: none;
  }
  .message-line {
    height: 28px;
    border-bottom: 2px dotted var(--rule);
  }
  .review-note {
    position: absolute;
    right: 50px;
    bottom: 18px;
    font-family: "Roboto", sans-serif;
    font-size: 14px;
    color: var(--ink-grey);
  }
  .review-note strong {
    font-weight: 500;
    color: var(--accent);
  }
</style>
</head>
<body>
<main class="canvas">
  <section class="card card-front" aria-label="Card front">
    <div class="motif-front" role="img" aria-label="Faint peach stripe motif"></div>
    <div class="brand">
      <span class="brand-square"></span>
      <span class="brand-name">QUILLFORGE</span>
    </div>
    <ul class="contact-list">
      <li class="contact-item"><span class="contact-dot"></span>@quillforge</li>
      <li class="contact-item"><span class="contact-dot"></span>@quillforge</li>
      <li class="contact-item">
        <svg class="contact-globe" viewBox="0 0 14 14" aria-hidden="true">
          <circle cx="7" cy="7" r="6" fill="none" stroke="#e8582a" stroke-width="1.4"/>
          <ellipse cx="7" cy="7" rx="2.6" ry="6" fill="none" stroke="#e8582a" stroke-width="1.2"/>
          <line x1="1" y1="7" x2="13" y2="7" stroke="#e8582a" stroke-width="1.2"/>
        </svg>www.quillforge-example.com
      </li>
    </ul>
  </section>

  <section class="card card-back" aria-label="Card back">
    <div class="motif-back" role="img" aria-label="Faint grey stripe motif"></div>
    <h1 class="thanks">
      <span class="thanks-title">Thanks</span>
      <span class="thanks-sub">For Your Order!</span>
    </h1>
    <ul class="message-lines" aria-label="Space for a handwritten message">
      <li class="message-line"></li>
      <li class="message-line"></li>
      <li class="message-line"></li>
      <li class="message-line"></li>
      <li class="message-line"></li>
    </ul>
    <p class="review-note">Enjoying it? Please <strong>leave us a review</strong> on Crafvine!</p>
  </section>
</main>
</body>
</html>
```